The Book Cover for "Finding the Silver Lantern of Dawn" needs redesigned

First the back ground or art work needs to be replaced or redesigned.
The title Finding the Silver Lantern of Dawn needs to be redesigned so that the words "Finding the" is diminished in size compared to the rest of the title "Silver Lantern of Dawn"
The Sub-title "Tracing the forgotten path of the Evening Wind" needs to be more pronounced and readable.
The authors name needs to be downsized.

```html
<!DOCTYPE html>
<html lang="en">
<head>
<meta charset="utf-8">
<title>Finding the Silver Lantern of Dawn — Cover</title>
<link rel="stylesheet" href="https://fonts.googleapis.com/css2?family=Alfa+Slab+One&family=Yellowtail&family=Satisfy&family=Josefin+Sans:wght@400&display=block">
<style>
  :root {
    --page: #ffffff;
    --sky: #8e9c9a;
    --sky-pale: #c3c7bb;
    --haze: #d8cdb2;
    --sun: #fffbec;
    --glow: #f3dcae;
    --gold: #b8925a;
    --amber: #9c7440;
    --foliage: #5c5034;
    --foliage-dark: #3b3422;
    --shade: #27231a;
    --grass: #6d6a48;
    --title: #ffffff;
    --subtitle: #efe4cf;
    --author: #e9c89a;
  }
  * { margin: 0; padding: 0; box-sizing: border-box; }
  html, body {
    width: 1200px;
    height: 846px;
    overflow: hidden;
    background: var(--page);
  }
  .canvas {
    position: relative;
    width: 1200px;
    height: 846px;
  }
  .cover {
    position: absolute;
    left: 347px;
    top: 43px;
    width: 505px;
    height: 760px;
    overflow: hidden;
    background: var(--foliage);
  }
  .cover-art {
    position: absolute;
    inset: 0;
    background:
      radial-gradient(circle at 83% 33%, var(--sun) 0%, rgba(255,246,220,0.95) 3%, rgba(243,220,174,0.6) 9%, rgba(0,0,0,0) 24%),
      radial-gradient(ellipse 40% 30% at 53% 66%, rgba(232,190,128,0.75) 0%, rgba(0,0,0,0) 100%),
      radial-gradient(ellipse 30% 22% at 30% 48%, rgba(220,200,160,0.55) 0%, rgba(0,0,0,0) 100%),
      radial-gradient(ellipse 45% 32% at 95% 8%, rgba(39,35,26,0.85) 0%, rgba(0,0,0,0) 100%),
      radial-gradient(ellipse 38% 30% at 100% 60%, rgba(59,52,34,0.85) 0%, rgba(0,0,0,0) 100%),
      radial-gradient(ellipse 30% 28% at 0% 60%, rgba(92,80,52,0.9) 0%, rgba(0,0,0,0) 100%),
      radial-gradient(ellipse 26% 20% at 8% 85%, rgba(59,52,34,0.8) 0%, rgba(0,0,0,0) 100%),
      radial-gradient(ellipse 22% 18% at 72% 58%, rgba(156,116,64,0.7) 0%, rgba(0,0,0,0) 100%),
      linear-gradient(180deg, rgba(0,0,0,0) 80%, rgba(109,106,72,0.7) 88%, rgba(39,35,26,0.85) 100%),
      linear-gradient(180deg, var(--sky) 0%, var(--sky-pale) 22%, var(--haze) 45%, var(--gold) 70%, var(--amber) 85%, var(--foliage-dark) 100%);
  }
  .cover-art::after {
    content: "";
    position: absolute;
    inset: 0;
    background:
      radial-gradient(ellipse 60% 12% at 50% 88%, rgba(240,215,170,0.35) 0%, rgba(0,0,0,0) 100%),
      linear-gradient(90deg, rgba(39,35,26,0.45) 0%, rgba(0,0,0,0) 18%, rgba(0,0,0,0) 78%, rgba(39,35,26,0.5) 100%);
  }
  .title {
    position: absolute;
    inset: 0;
    font-family: "Alfa Slab One", serif;
    font-weight: 400;
    color: var(--title);
  }
  .title-lead {
    position: absolute;
    left: 128px;
    top: 60px;
    font-size: 38px;
    line-height: 1;
    white-space: nowrap;
  }
  .title-lead .title-article { font-size: 24px; }
  .title-main {
    position: absolute;
    left: 22px;
    top: 106px;
    font-size: 60px;
    line-height: 1.12;
    white-space: nowrap;
  }
  .title-main span { display: block; }
  .subtitle {
    position: absolute;
    left: 0;
    top: 618px;
    width: 100%;
    text-align: center;
    font-family: "Yellowtail", "Satisfy", cursive;
    font-size: 33px;
    line-height: 1.0;
    color: var(--subtitle);
  }
  .subtitle span { display: block; }
  .author {
    position: absolute;
    left: 0;
    top: 718px;
    width: 100%;
    text-align: center;
    font-family: "Josefin Sans", sans-serif;
    font-variant: small-caps;
    font-size: 15px;
    letter-spacing: 0.5px;
    color: var(--author);
  }
</style>
</head>
<body>
  <main class="canvas">
    <article class="cover">
      <div class="cover-art" role="img" aria-label="Silhouette of a woman lifting a small child in a sunlit, misty woodland with sunrays through the trees"></div>
      <h1 class="title">
        <span class="title-lead">Finding <span class="title-article">the</span></span>
        <span class="title-main"><span>Silver Lantern</span><span>of Dawn</span></span>
      </h1>
      <p class="subtitle"><span>Tracing the forgotten path</span><span>of the Evening Wind</span></p>
      <p class="author">R J Alder Whitcombe</p>
    </article>
  </main>
</body>
</html>
```